Stationery Design Project

I am a personal trainer in the fitness industry based in Miami. I have recently designed a logo for my company, now i need to market my name through selected stationery designs.
I need an email signature, invoice and a business card. I am looking for a design that is fresh and eye catching to my target audience.
Updates

Reason: Waiting for photo to be taken for business card.

Target Market(s)

25 to 65 years old - male and female - overweight, sedentary and athletic clientele - middle to wealthy economic class

Industry/Entity Type

Personal Trainer

Requirements
Must have
• Will attach Zip file with logo, template of invoice and personal information.
Will attach photo for business card in the next few days.
Nice to have
• Black backdrop logo image for banner of Invoice, with transparent images of my logo.
White backdrop logo image for Email signature, with font that works well with logo.

```html
<!DOCTYPE html>
<html lang="en">
<head>
<meta charset="utf-8">
<title>Kinetic Form Studio – Stationery Set</title>
<link href="https://fonts.googleapis.com/css2?family=Open+Sans:wght@400;600;700;800&family=Source+Sans+3:wght@400;600;700&display=swap" rel="stylesheet">
<style>
  :root{
    --ink:#000;
    --paper:#fff;
    --brand:#f39a1e;
    --gold:#f6b81c;
    --grey:#5f6062;
    --line:#333;
  }
  *{box-sizing:border-box;margin:0;padding:0}
  html,body{width:1200px;height:900px;overflow:hidden;background:var(--paper)}
  body{position:relative;font-family:"Source Sans 3",Arial,sans-serif;color:var(--ink)}
  .abs{position:absolute}
  .section-label{position:absolute;font-family:"Open Sans",Arial,sans-serif;font-weight:800;font-size:16px;letter-spacing:.3px}
  .sheet{position:absolute;border:1px solid var(--ink);background:var(--paper);z-index:1}
  .banner{position:absolute;background:var(--ink);display:flex;align-items:center;justify-content:space-between;padding:0 16px 0 14px}
  .brand{display:flex;align-items:center;gap:7px;color:var(--brand);font-family:"Source Sans 3",Arial,sans-serif;font-weight:700;line-height:1;text-transform:uppercase}
  .brand-dot{border-radius:50%;background:var(--brand);flex:none}
  .banner .brand{font-size:17px}
  .banner .brand-dot{width:22px;height:22px}
  .banner-title{font-weight:700;color:var(--gold);font-size:17px}
  .banner-name{font-weight:700;color:var(--brand);font-size:15px}

  .from-block{position:absolute;left:40px;top:94px;font-size:6.4px;line-height:8.6px}
  .from-block .email{font-style:italic}
  .inv-meta{position:absolute;right:40px;top:140px;font-size:5.5px;line-height:8px;text-align:right;color:#444}
  .location{position:absolute;left:40px;top:161px;font-size:6.5px}
  .bill{position:absolute;left:40px;top:181px;font-size:5.5px;line-height:7.2px}
  .bill b{display:inline-block;width:62px}

  .items{position:absolute;left:36px;top:238px;width:341px;height:196px;border:1px solid var(--line)}
  .items-head{height:12px;background:var(--ink);color:var(--gold);font-size:5.5px;font-weight:700;position:relative}
  .items-head span,.items-row span{position:absolute;top:3px}
  .col{position:absolute;top:0;bottom:0;border-left:1px solid var(--line)}
  .items-foot{position:absolute;left:0;right:0;top:181px;border-top:1px solid var(--line)}
  .items-row{position:relative;font-size:5.2px;line-height:6px}
  .totals{position:absolute;left:285px;top:434px;font-size:4.8px;font-weight:700}
  .totals div{position:relative;height:13px}
  .totals .val{position:absolute;left:36px;top:0;width:56px;height:13px;border:1px solid var(--line);border-top:none;text-align:right;padding:3px 4px;font-weight:400}
  .totals .lab{position:absolute;left:0;top:4px;width:32px;text-align:right}
  .checks{position:absolute;left:40px;top:437px;font-size:7.5px}
  .thanks{position:absolute;left:40px;top:465px;font-size:9.2px}

  .card{position:absolute;background:var(--ink);color:var(--paper);text-align:center;z-index:2}
  .card-front{display:flex;align-items:center;justify-content:center}
  .card-front .brand{flex-direction:column;font-size:15px;gap:10px;text-align:center}
  .card-front .brand-dot{width:40px;height:40px}
  .card-name{color:var(--brand);font-weight:700}

  .lh-footer{position:absolute;left:0;right:0;top:486px;text-align:center;font-size:10px;line-height:12px;color:var(--grey)}
  .envelope{position:absolute;border:1px solid var(--ink);background:var(--paper);overflow:hidden}
  .env-band{position:absolute;left:0;right:0;top:0;height:14px;background:var(--ink)}
</style>
</head>
<body>

<h2 class="section-label" style="left:36px;top:38px">INVOICE</h2>
<h2 class="section-label" style="left:503px;top:32px">3.5X3.5 INCH BUS CARD</h2>
<h2 class="section-label" style="left:750px;top:38px">LETTERHEAD</h2>
<h2 class="section-label" style="left:510px;top:446px">STANDARD BUS CARD</h2>

<!-- Invoice -->
<section class="sheet invoice" style="left:36px;top:78px;width:414px;height:536px">
  <div class="banner" style="left:25px;top:25px;width:365px;height:55px">
    <div class="brand"><span class="brand-dot"></span>Kinetic Form Studio</div>
    <div class="banner-title">INVOICE</div>
  </div>
  <div class="from-block">
    Dana Reyes<br>248 Harbor Lane<br># 1204<br>Miami, FL 33130<br>Home 305-555-0142<br>Cell&nbsp;&nbsp;&nbsp; 508-555-0187<br>
    <span class="email">dana@kineticformstudio.com</span>
  </div>
  <div class="inv-meta">INVOICE # 0000<br>DATE: 00/00/2012</div>
  <div class="location">Training Location: The Seaview</div>
  <div class="bill">
    <b>BILL</b>XXXXXXXXXXX<br><b>TO</b>XXXXXXXXXXX<br><b></b>XXXXX, FL<br><b></b>XXXXX
  </div>
  <div class="items">
    <div class="items-head">
      <span style="left:14px">QTY</span>
      <span style="left:118px">DESCRIPTION</span>
      <span style="left:243px">UNIT PRICE</span>
      <span style="left:297px">LINE TOTAL</span>
    </div>
    <div class="items-row">
      <span style="left:4px;top:2px">Session<br>Package</span>
      <span style="left:46px;top:6px">Personal Training</span>
      <span style="left:268px;top:6px">$00</span>
      <span style="left:320px;top:6px">$000</span>
    </div>
    <div class="col" style="left:42px"></div>
    <div class="col" style="left:230px"></div>
    <div class="col" style="left:284px"></div>
    <div class="items-foot"></div>
  </div>
  <p class="checks">Please make all checks payable to Dana Reyes.</p>
  <p class="thanks">THANK YOU FOR YOUR BUSINESS!</p>
  <div class="totals">
    <div><span class="lab">SUBTOTAL</span><span class="val">$000.00</span></div>
    <div><span class="lab">SALES TAX</span><span class="val">-</span></div>
    <div><span class="lab">TOTAL</span><span class="val">$000.00</span></div>
  </div>
</section>

<!-- Square card -->
<div class="card card-front" style="left:515px;top:73px;width:170px;height:170px">
  <div class="brand"><span class="brand-dot"></span>Kinetic Form<br>Studio</div>
</div>
<div class="card" style="left:515px;top:256px;width:170px;height:170px;font-size:9.5px;line-height:12px">
  <div class="card-name" style="font-size:14px;margin-top:24px">Dana Reyes</div>
  <p style="margin-top:10px">H 305-555-0142</p>
  <p style="margin-top:10px">C 508-555-0187</p>
  <p style="margin-top:10px">dana@kineticformstudio.com</p>
  <p style="margin-top:10px">248 Harbor Lane<br>#1204<br>Miami, FL 33130</p>
</div>

<!-- Letterhead -->
<section class="sheet letterhead" style="left:750px;top:78px;width:415px;height:536px">
  <div class="banner" style="left:24px;top:25px;width:367px;height:55px">
    <div class="brand"><span class="brand-dot"></span>Kinetic Form Studio</div>
    <div class="banner-name" style="margin-right:14px">Dana Reyes</div>
  </div>
  <p class="lh-footer">H 305-555-0142 • C 508-555-0187 • dana@kineticformstudio.com<br>248 Harbor Lane #1204, Miami, FL 33130</p>
</section>

<!-- Standard card (sits above the letterhead edge) -->
<div class="card card-front" style="left:433px;top:487px;width:171px;height:97px">
  <div class="brand" style="flex-direction:row;font-size:12px;gap:6px"><span class="brand-dot" style="width:20px;height:20px"></span>Kinetic Form Studio</div>
</div>
<div class="card" style="left:613px;top:487px;width:170px;height:97px;font-size:7.6px;line-height:10px">
  <div class="card-name" style="font-size:11px;margin-top:21px">Dana Reyes</div>
  <p style="margin-top:7px">H 305-555-0142 • C 508-555-0187<br>dana@kineticformstudio.com</p>
  <p style="margin-top:7px;font-size:5.6px">248 Harbor Lane • # 1204 • Miami, FL 33130</p>
</div>

<!-- Envelope front -->
<section class="envelope" style="left:71px;top:640px;width:515px;height:223px">
  <div class="env-band"></div>
  <div class="brand abs" style="left:17px;top:25px;font-size:11px;gap:5px"><span class="brand-dot" style="width:14px;height:14px"></span>Kinetic Form Studio</div>
  <p class="abs" style="left:16px;top:55px;font-size:7.2px;line-height:9px;color:var(--grey)">248 Harbor Lane #1204<br>Miami, FL 33130</p>
</section>

<!-- Envelope back -->
<section class="envelope" style="left:614px;top:640px;width:515px;height:223px">
  <svg class="abs" style="left:0;top:0" width="515" height="100" viewBox="0 0 515 100" aria-hidden="true">
    <path d="M0 0 H515 V4 C505 30 495 36 440 52 C360 74 320 95 257 95 C194 95 154 74 74 52 C20 36 10 30 0 4 Z" fill="#000"/>
  </svg>
  <div class="brand abs" style="left:0;right:0;top:24px;flex-direction:column;font-size:10px;gap:6px;text-align:center">
    <span class="brand-dot" style="width:22px;height:22px"></span>Kinetic Form Studio
  </div>
</section>

</body>
</html>
```